A golden web-design opportunity

I have created a quick website (www.brintavexgroup.com.au) but I would like to have the website “polished” to look more professional and have a better consistency.

I would like the website to come across as a genuine, professional insight into our business culture but unfortunately my creative skills have reached their limit.

I have attached a media kit PDF so you are better able to establish what are about.
Updates

Hello All! I just wanted to let everyone know that I do not require an ecommerce site! My website is for potential clients to visit, see what we do and get my contact details...

Gathering more feedback

Hello All, I just wanted to let contestants know that there is not a requirement for my team to be mentioned on the website. I cover in person this as part of my presentation with clients. I have uploaded a new Presentation PDF that has this information excluded. Have a good day!

Target Market(s)

Telecommunications professionals; service delivery partners; white collar executives; construction

Industry/Entity Type

Data Communication

Coding

Coded - Design and coding required

Number of Pages Required

3 page

Font styles to use
Other font styles liked:
• Designers discretion

Colors

Designer to choose colors to be used in the design.

Requirements
Must have
• Must be designed so that I can upload it to Plesk, I think that wordpress is preferred.
• - Page:
• - 1 - Full page is a requirement i.e. the website makes full use of the whole screen
• - 2 - Colour scheme must be "muted" and not agressive
• - Links:
• - 1 - All links will work e.g. "E-Mail us" should work
• - 2 - The page identifier ("[LOGO] Home | Brintavex Gruop) will show the Brintavex logo
• - 3 - A link to facebook and linkedin
• - https://www.facebook.com/brintavexgroup
• - https://www.linkedin.com/company/brintavex-group-pty-ltd/
• - 4 - The phone number icon can be clicked on to make a call
• - 5 - The E-Mail icon can be clicked on to send an E-Mail
Nice to have
• Font:
• - 1 - Rounded is preferred
• - 2 - Colour with reference the logo colours (if possible)
Should not have
• Colour:
• - 1 - To much contrast between colours i.e. balck background with white writing
• - 2 - aggressive colour schemes
• - 3 - Names of Brintavex consultants... These guys are also used by my competetion, only martin is required

```html
<!DOCTYPE html>
<html lang="en">
<head>
<meta charset="utf-8">
<title>Home | Brintavex Solutions</title>
<link href="https://fonts.googleapis.com/css2?family=Raleway:wght@400;500;600;700&family=Open+Sans:wght@400;600;700&display=swap" rel="stylesheet">
<style>
:root{
  --ink:#000;
  --panel:#0b0b0b;
  --teal:#2a8caf;
  --teal-deep:#1d7596;
  --teal-soft:#3aa3c6;
  --white:#fff;
  --muted:#c9d6dc;
  --text-dark:#333;
  --head:'Raleway',sans-serif;
  --body:'Open Sans',sans-serif;
}
*{box-sizing:border-box;margin:0;padding:0}
html,body{width:1200px;height:3480px;overflow:hidden;background:var(--ink);font-family:var(--body);color:var(--white)}
.page{position:relative;width:1200px;height:3480px}
a{color:inherit;text-decoration:none}

/* top bar */
.topbar{position:absolute;top:0;left:0;width:1200px;height:32px;background:rgba(0,0,0,.55);display:flex;align-items:center;justify-content:space-between;padding:0 40px;font-size:12px;z-index:3}
.topbar .phone{position:absolute;left:50%;transform:translateX(-50%)}
.social{display:flex;gap:8px}
.social span{width:14px;height:14px;border-radius:50%;background:var(--white);display:block}

/* nav */
.nav{position:absolute;top:44px;left:0;width:1200px;height:64px;display:flex;align-items:center;justify-content:space-between;padding:0 40px;z-index:3}
.brand{display:flex;align-items:center;gap:10px;font-family:var(--head);font-weight:700;font-size:24px;color:var(--white)}
.brand i{width:34px;height:34px;border-radius:50%;background:var(--teal-soft);display:block}
.menu{display:flex;gap:32px;font-family:var(--head);font-weight:600;font-size:15px}

/* hero */
.hero{position:absolute;top:0;left:0;width:1200px;height:780px;overflow:hidden}
.hero-photo{position:absolute;inset:0;background:radial-gradient(ellipse at 60% 35%,#8a9aa6 0%,#4e5e6b 35%,#1f2a33 75%,#0d1217 100%)}
.hero-copy{position:absolute;top:395px;width:100%;text-align:center}
.hero-copy h1{font-family:var(--head);font-weight:500;font-size:44px;letter-spacing:.5px}
.hero-copy p{font-size:14px;margin-top:10px;color:var(--muted)}
.btn{display:inline-block;background:var(--teal);color:var(--white);font-size:13px;font-weight:600;padding:10px 30px;border-radius:4px}
.btn.dark{background:#000}
.hero-copy .btn{margin-top:22px}
.hero-wave{position:absolute;bottom:0;left:0}

/* services */
.services{position:absolute;top:780px;left:0;width:1200px;height:860px;background:var(--ink);text-align:center}
.section-title{font-family:var(--head);font-weight:500;font-size:34px}
.rule{width:60px;height:2px;background:var(--white);margin:12px auto 0}
.services .section-title{margin-top:60px}
.intro{width:720px;margin:20px auto 0;font-size:13px;line-height:1.6;color:var(--muted)}
.service-grid{position:absolute;top:240px;left:120px;width:960px;display:grid;grid-template-columns:repeat(3,1fr);grid-auto-rows:170px;row-gap:30px}
.service{height:170px;display:flex;flex-direction:column;align-items:center;justify-content:center;font-family:var(--head);font-size:18px;font-weight:500;line-height:1.25}
.service svg{margin-bottom:14px}
.service.active{background:var(--teal);border-radius:8px;width:280px;height:200px;justify-self:center;align-self:center}
.service.active svg{margin-bottom:10px}
.service.active p{font-family:var(--body);font-size:12px;color:#e4f1f6;width:210px;margin-top:8px;line-height:1.5}
.service.active .more{font-family:var(--body);font-size:12px;font-weight:700;margin-top:10px}

/* story */
.story{position:absolute;top:1640px;left:0;width:1200px;height:620px;background:var(--teal);text-align:center}
.story-wave{position:absolute;top:-40px;left:0}
.story .section-title{margin-top:60px}
.story .intro{color:#e6f3f8;width:620px}
.story .btn{margin-top:22px}
.story-row{position:absolute;top:250px;left:120px;width:960px;display:flex;justify-content:space-between}
.story-item{width:290px}
.story-item .ph{height:230px;border:4px solid #0c5d7a}
.story-item h3{font-family:var(--head);font-weight:500;font-size:26px;margin-top:18px}

/* blogs */
.blogs{position:absolute;top:2260px;left:0;width:1200px;height:580px;background:var(--ink);text-align:center}
.blogs .section-title{margin-top:48px}
.blog-row{position:absolute;top:130px;left:120px;width:960px;display:flex;justify-content:space-between}
.card{width:300px;background:var(--white);text-align:left;color:var(--text-dark)}
.card .ph{height:200px}
.card .body{padding:12px 14px 16px}
.meta{display:flex;justify-content:space-between;font-size:11px;font-weight:600;color:#555}
.card h4{font-family:var(--head);font-size:15px;margin-top:10px;color:#222}
.card p{font-size:11px;line-height:1.5;margin-top:6px;color:#666}
.card .more{font-size:12px;font-weight:700;margin-top:10px;display:block;color:#222}
.blogs .btn{position:absolute;top:510px;left:50%;transform:translateX(-50%)}

/* newsletter */
.newsletter{position:absolute;top:2840px;left:0;width:1200px;height:160px;text-align:center}
.newsletter h2{font-family:var(--head);font-weight:500;font-size:26px}
.newsletter p{font-size:12px;color:var(--muted);margin-top:4px}
.signup{display:flex;width:500px;margin:22px auto 0}
.signup span{flex:1;height:34px;background:var(--ink);border:1px solid #555;font-size:12px;color:#aaa;text-align:left;padding:9px 12px}
.signup b{width:120px;height:34px;background:var(--teal);font-size:12px;font-weight:600;padding-top:9px}

/* footer */
.footer{position:absolute;top:3000px;left:0;width:1200px;height:400px;background:var(--teal-deep)}
.footer-wave{position:absolute;top:0;left:0}
.footer-cols{position:absolute;top:140px;left:120px;width:960px;display:flex}
.f-about{width:300px}
.f-about p{font-size:12px;line-height:1.6;margin-top:16px;font-weight:600}
.f-about .more{font-size:12px;font-weight:700;margin-top:8px;display:block}
.f-col{width:190px;padding-left:20px}
.f-col h5,.f-form h5{font-family:var(--head);font-size:13px;font-weight:700;border-bottom:1px solid var(--white);padding-bottom:4px;display:inline-block}
.f-col ul{list-style:none;margin-top:20px;font-size:12px;line-height:2}
.f-col ul li:before{content:"› "}
.f-col address{font-style:normal;margin-top:20px;font-size:12px;line-height:1.8}
.f-form{width:280px;padding-left:20px}
.f-form .fields{display:grid;grid-template-columns:1fr 1fr;gap:8px;margin-top:20px}
.f-form .fields span{height:22px;background:var(--white);border-radius:3px;font-size:10px;color:#888;padding:4px 6px}
.f-form .fields .msg{grid-column:span 2;height:48px}
.f-form b{display:inline-block;margin-top:10px;background:#000;color:var(--white);font-size:11px;padding:6px 18px;border-radius:3px}
.f-social{position:absolute;top:336px;right:120px;display:flex;gap:10px}
.f-social span{width:22px;height:22px;border-radius:50%;background:var(--white)}
.copyright{position:absolute;top:3400px;left:0;width:1200px;height:80px;background:var(--ink);display:flex;align-items:center;padding-left:120px;font-size:13px;font-weight:600}
</style>
</head>
<body>
<div class="page">

  <section class="hero">
    <div class="hero-photo" role="img" aria-label="Photo of people at a desk reviewing documents beside a laptop"></div>
    <div class="hero-copy">
      <h1>Brintavex Solution</h1>
      <p>Project Delivery Done Differently</p>
      <a class="btn" href="#story">Read More</a>
    </div>
    <svg class="hero-wave" width="1200" height="120" viewBox="0 0 1200 120">
      <path d="M0 70 C300 20 520 110 800 70 S1100 30 1200 55 L1200 120 L0 120Z" fill="#000"/>
      <path d="M0 62 C300 12 520 102 800 62 S1100 22 1200 47" fill="none" stroke="#2a8caf" stroke-width="3"/>
      <path d="M0 78 C320 30 540 116 820 78 S1110 40 1200 64" fill="none" stroke="#1d7596" stroke-width="2"/>
    </svg>
  </section>

  <div class="topbar">
    <a href="mailto:info@brintavex.co">info@brintavex.co</a>
    <a class="phone" href="tel:+61400555019">+61 400 555 019</a>
    <div class="social"><span></span><span></span><span></span><span></span></div>
  </div>

  <nav class="nav">
    <a class="brand" href="#"><i></i>Brintavex Solutions</a>
    <div class="menu"><a href="#">Home</a><a href="#story">Our Story</a><a href="#services">Services</a><a href="#blogs">Blogs</a><a href="#contact">Contacts</a></div>
  </nav>

  <section class="services" id="services">
    <h2 class="section-title">Our Services</h2>
    <div class="rule"></div>
    <p class="intro">Working with Brintavex Solutions gives you a single point of contact for your entire project. We have a wide range of specialists under one roof that allows us to take on full responsibility for every project.<br>Working with Brintavex Solutions reduces delays, duplication and time to complete the project.</p>
    <div class="service-grid">
      <div class="service">
        <svg width="56" height="56" viewBox="0 0 64 64" fill="none" stroke="#fff" stroke-width="3"><rect x="14" y="10" width="34" height="46" rx="3"/><path d="M22 24h18M22 34h18M22 44h12"/><circle cx="46" cy="46" r="9"/></svg>
        Project<br>Management
      </div>
      <div class="service active">
        <svg width="48" height="48" viewBox="0 0 64 64" fill="none" stroke="#fff" stroke-width="3"><path d="M12 10v44M24 10v44M36 10v44M48 10v44M8 22h48M8 42h48"/></svg>
        Asbestos Removal
        <p>Safe handling and disposal of hazardous materials on every site.</p>
        <span class="more">Continue ›</span>
      </div>
      <div class="service">
        <svg width="56" height="56" viewBox="0 0 64 64" fill="none" stroke="#fff" stroke-width="3"><path d="M6 26h20v12H6M58 26H38v12h20M26 32h12M32 16v10M24 14h16"/></svg>
        Pit and Pipe<br>Installation
      </div>
      <div class="service">
        <svg width="56" height="56" viewBox="0 0 64 64" fill="none" stroke="#fff" stroke-width="3"><rect x="20" y="10" width="24" height="40" rx="4"/><path d="M20 20h24M20 30h24M20 40h24M32 50v8"/></svg>
        Cable Hauling
      </div>
      <div class="service">
        <svg width="56" height="56" viewBox="0 0 64 64" fill="none" stroke="#fff" stroke-width="3"><path d="M32 8v20M32 36v20M10 32h16M38 32h16M16 16l12 12M36 36l12 12"/></svg>
        Fibre splicing
      </div>
      <div class="service">
        <svg width="56" height="56" viewBox="0 0 64 64" fill="none" stroke="#fff" stroke-width="3"><path d="M10 54l20-20M30 34l6-14 14-6-6 14zM40 40l14 14"/></svg>
        Copper Jointing
      </div>
      <div class="service">
        <svg width="56" height="56" viewBox="0 0 64 64" fill="none" stroke="#fff" stroke-width="3"><path d="M32 8c-8 10-8 18 0 24s8 14 0 24M20 14c-6 12-6 24 0 36M44 14c6 12 6 24 0 36"/></svg>
        Fibre Integration
      </div>
      <div class="service">
        <svg width="56" height="56" viewBox="0 0 64 64" fill="none" stroke="#fff" stroke-width="3"><path d="M52 32a20 20 0 1 1-6-14"/><path d="M48 8v12H36"/></svg>
        Recoverable works
      </div>
      <div class="service">
        <svg width="56" height="56" viewBox="0 0 64 64" fill="none" stroke="#fff" stroke-width="3"><path d="M32 24l-12 34M32 24l12 34M24 46h16"/><circle cx="32" cy="20" r="4"/><path d="M22 12a14 14 0 0 0 0 16M42 12a14 14 0 0 1 0 16"/></svg>
        Telecommunication Rigging
      </div>
    </div>
  </section>

  <section class="story" id="story">
    <svg class="story-wave" width="1200" height="60" viewBox="0 0 1200 60"><path d="M0 40 C300 0 600 60 900 30 S1150 20 1200 35 L1200 60 L0 60Z" fill="#2a8caf"/></svg>
    <h2 class="section-title">Our Story</h2>
    <div class="rule"></div>
    <p class="intro">We are an innovative telecommunications services company. We believe technology can truly change peoples' lives, so we are working with the industry's most respected delivery partners to complete unique projects team wide.</p>
    <a class="btn dark" href="#">Read More</a>
    <div class="story-row">
      <div class="story-item"><div class="ph" role="img" aria-label="Photo of a network test instrument on a rack" style="background:linear-gradient(160deg,#3c6f8f,#1c2c3a)"></div><h3>Innovation</h3></div>
      <div class="story-item"><div class="ph" role="img" aria-label="Photo of hands joined together in teamwork" style="background:linear-gradient(160deg,#d9b59a,#8a6a58)"></div><h3>Collaboration</h3></div>
      <div class="story-item"><div class="ph" role="img" aria-label="Photo of yellow hard hats on a table" style="background:linear-gradient(160deg,#c9d2d6,#c7b23a)"></div><h3>Integrity</h3></div>
    </div>
  </section>

  <section class="blogs" id="blogs">
    <h2 class="section-title">Blogs</h2>
    <div class="rule"></div>
    <div class="blog-row">
      <article class="card"><div class="ph" role="img" aria-label="Photo of a worker on a construction site" style="background:linear-gradient(160deg,#7e8f9a,#3d4a52)"></div>
        <div class="body"><div class="meta"><span>July 01, 2018</span><span>20 &nbsp; 12</span></div><h4>Blog Post Title to</h4><p>Lorem ipsum is simply dummy text of the printing and typesetting.</p><a class="more" href="#">Continue ›</a></div></article>
      <article class="card"><div class="ph" role="img" aria-label="Photo of a technician working on equipment" style="background:linear-gradient(160deg,#5a5148,#2a2622)"></div>
        <div class="body"><div class="meta"><span>June 01, 2018</span><span>20 &nbsp; 12</span></div><h4>Blog Post Title to</h4><p>Lorem ipsum is simply dummy text of the printing and typesetting.</p><a class="more" href="#">Continue ›</a></div></article>
      <article class="card"><div class="ph" role="img" aria-label="Photo of hands splicing network cables" style="background:linear-gradient(160deg,#4f7d8e,#2f3d30)"></div>
        <div class="body"><div class="meta"><span>June 01, 2018</span><span>20 &nbsp; 12</span></div><h4>Blog Post Title to</h4><p>Lorem ipsum is simply dummy text of the printing and typesetting.</p><a class="more" href="#">Continue ›</a></div></article>
    </div>
    <a class="btn" href="#">View More</a>
  </section>

  <section class="newsletter">
    <h2>Join The Newsletter</h2>
    <p>Sign up for Our Newsletter</p>
    <div class="signup"><span>Email Here</span><b>Subscribe</b></div>
  </section>

  <footer class="footer" id="contact">
    <svg class="footer-wave" width="1200" height="100" viewBox="0 0 1200 100">
      <path d="M0 0 H1200 V30 C1000 80 750 10 500 50 S150 70 0 40Z" fill="#000"/>
      <path d="M0 46 C150 76 300 60 500 56 S1000 86 1200 36" fill="none" stroke="#3aa3c6" stroke-width="3"/>
    </svg>
    <div class="footer-cols">
      <div class="f-about">
        <a class="brand" href="#"><i></i>Brintavex Solutions</a>
        <p>Lorem Ipsum is simply dummy text of the printing and typesetting industry. Lorem Ipsum has been the standard dummy text.</p>
        <a class="more" href="#">Read More ›</a>
      </div>
      <div class="f-col"><h5>QUICK LINKS</h5><ul><li>Home</li><li>Our Story</li><li>Services</li><li>Blogs</li><li>Contacts</li></ul></div>
      <div class="f-col"><h5>CONTACT US</h5><address>48 Harlow Street,<br>Sydney NSW 2000<br>Australia<br><a href="tel:+61400555019">+61 400 555 019</a><br><a href="mailto:info@brintavex.co">info@brintavex.co</a></address></div>
      <div class="f-form"><h5>QUICK CONTACT</h5>
        <div class="fields"><span>Name</span><span>Email</span><span class="msg">Message</span></div><b>Send</b></div>
    </div>
    <div class="f-social"><span></span><span></span><span></span><span></span></div>
  </footer>
  <div class="copyright">Copyright © 2018 Brintavex Solutions. All Rights Reserved.</div>
</div>
</body>
</html>
```